" Trabalhamos com vistorias profissionais de imóveis. Um vistoriador (engenheiro civil ou alguém com experiência em obras e entregas de imóveis) analisa detalhadamente o imóvel, buscando e relatando vícios construtivos. Todo trabalho é documentado através de relatório, que servirá de garantia futura para as partes interessadas. Nossa ideia principal é a de que vistoriar corretamente um imóvel pode significar enorme economia e evitar muita dor de cabeça futura. "

```html
<!DOCTYPE html>
<html lang="pt-BR">
<head>
<meta charset="UTF-8">
<title>Assinatura de e-mail – Casa Aferida</title>
<link rel="stylesheet" href="https://fonts.googleapis.com/css2?family=Montserrat:wght@500;600;700&family=Open+Sans:wght@400;600;700&display=swap">
<style>
  :root {
    --navy: #1f2a5c;
    --orange: #e07a2e;
    --ink: #1c2345;
    --paper: #ffffff;
    --backdrop: #eef0f3;
  }
  * { margin: 0; padding: 0; box-sizing: border-box; }
  html, body {
    width: 1200px; height: 1200px; overflow: hidden;
    background: var(--backdrop);
  }
  .canvas {
    position: relative; width: 1200px; height: 1200px;
    display: flex; align-items: center; justify-content: center;
  }
  .signature {
    position: relative; width: 1000px; height: 284px;
    box-shadow: 0 6px 18px rgba(20, 30, 60, 0.18);
  }
  .signature-frame { position: absolute; inset: 0; }
  .contact-block {
    position: absolute; left: 82px; top: 38px; width: 280px;
    font-family: "Open Sans", sans-serif; color: var(--ink);
  }
  .person-name {
    font-size: 30px; font-weight: 700; color: var(--navy);
    padding-bottom: 6px; border-bottom: 2px solid var(--navy);
    width: 285px;
  }
  .person-role {
    font-size: 17px; font-weight: 700; margin-top: 10px;
  }
  .contact-row {
    display: flex; align-items: flex-start; gap: 18px; margin-top: 22px;
    font-size: 18px; line-height: 1.3;
  }
  .contact-row + .contact-row { margin-top: 14px; }
  .contact-icon { width: 26px; height: 26px; flex: none; margin-top: 6px; }
  .web-line { display: flex; align-items: center; gap: 10px; font-weight: 700; }
  .social-dots { display: flex; gap: 4px; }
  .social-dot { width: 16px; height: 16px; border-radius: 50%; background: var(--navy); }
  .divider {
    position: absolute; left: 385px; top: 42px; width: 3px; height: 200px;
    background: var(--orange);
  }
  .brand {
    position: absolute; left: 420px; right: 40px; top: 0; bottom: 0;
    display: flex; align-items: center; justify-content: center; gap: 20px;
  }
  .brand-dot { width: 64px; height: 64px; border-radius: 50%; background: var(--orange); flex: none; }
  .brand-name {
    font-family: "Montserrat", sans-serif; font-weight: 700;
    font-size: 60px; letter-spacing: 1px; color: var(--navy); text-transform: uppercase;
  }
</style>
</head>
<body>
<main class="canvas">
  <section class="signature" aria-label="Assinatura de e-mail">
    <svg class="signature-frame" viewBox="0 0 1000 284" width="1000" height="284" aria-hidden="true">
      <rect x="0" y="0" width="1000" height="284" fill="var(--navy)"/>
      <path d="M20 40 Q20 14 60 14 L920 14 Q980 14 986 70 L986 250 Q986 270 966 270 L20 270 Z" fill="var(--paper)"/>
      <path d="M760 284 Q900 284 940 214 Q960 180 1000 170 L1000 284 Z" fill="var(--navy)"/>
    </svg>

    <div class="contact-block">
      <p class="person-name">Nome Sobrenome</p>
      <p class="person-role">Cargo Nome</p>
      <div class="contact-row">
        <svg class="contact-icon" viewBox="0 0 24 24" aria-hidden="true">
          <path d="M6.6 10.8a15 15 0 0 0 6.6 6.6l2.2-2.2a1 1 0 0 1 1-.25 11.4 11.4 0 0 0 3.6.57 1 1 0 0 1 1 1V20a1 1 0 0 1-1 1A17 17 0 0 1 3 4a1 1 0 0 1 1-1h3.5a1 1 0 0 1 1 1c0 1.25.2 2.45.57 3.57a1 1 0 0 1-.25 1z" fill="var(--ink)"/>
        </svg>
        <div>
          <p>+ 55 00 90000 0000</p>
          <p>+ 55 00 0000 0000</p>
        </div>
      </div>
      <div class="contact-row">
        <svg class="contact-icon" viewBox="0 0 24 24" aria-hidden="true">
          <g fill="none" stroke="var(--ink)" stroke-width="1.8">
            <circle cx="12" cy="12" r="9.5"/>
            <ellipse cx="12" cy="12" rx="4" ry="9.5"/>
            <path d="M2.5 12h19M4 7h16M4 17h16"/>
          </g>
        </svg>
        <div>
          <p>contato@site.com.br</p>
          <p class="web-line">www.site.com.br
            <span class="social-dots"><span class="social-dot"></span><span class="social-dot"></span></span>
          </p>
        </div>
      </div>
    </div>

    <div class="divider"></div>

    <div class="brand">
      <span class="brand-dot"></span>
      <span class="brand-name">Casa Aferida</span>
    </div>
  </section>
</main>
</body>
</html>
```